Construction Company Needs Letterhead Design

We recently had a new logo designed and would like to have our letterhead updated to a trendier design. We are a concrete construction company based out of Iowa, but do work for Agricultural businesses across the Midwest.

Industry/Entity Type

Construction

Colors
ec1f27
000000
ffffff

Requirements
Must have
• Must stay within our current color scheme of red/black/white. Must have have our address, phone number, e-mail address, etc. printed on the letterhead as well.

```html
<!DOCTYPE html>
<html lang="en">
<head>
<meta charset="utf-8">
<title>Harrowfield Letterhead</title>
<link rel="stylesheet" href="https://fonts.googleapis.com/css2?family=Source+Sans+3:wght@400;700&display=swap">
<style>
  :root {
    --brand-red: #ec1f27;
    --brand-black: #000000;
    --paper: #ffffff;
    --header-tint: #fce7e9;
    --footer-tint: #f2f2f2;
    --text: #1a1a1a;
  }
  html, body {
    margin: 0;
    padding: 0;
    overflow: hidden;
    background: var(--paper);
  }
  .letterhead {
    position: relative;
    width: 927px;
    height: 1200px;
    overflow: hidden;
    background: var(--paper);
    font-family: "Source Sans 3", sans-serif;
  }
  .letterhead__bands {
    position: absolute;
    inset: 0;
  }
  .header-band { fill: var(--header-tint); }
  .footer-band { fill: var(--footer-tint); }
  .brand {
    position: absolute;
    left: 34px;
    top: 38px;
    display: flex;
    align-items: center;
    gap: 16px;
  }
  .brand__mark {
    width: 58px;
    height: 58px;
    background: var(--brand-red);
  }
  .brand__name {
    font-size: 60px;
    font-weight: 700;
    line-height: 1;
    letter-spacing: 1px;
    color: var(--brand-black);
    text-transform: uppercase;
  }
  .contact {
    position: absolute;
    left: 0;
    right: 0;
    top: 1100px;
    text-align: center;
    font-size: 21px;
    line-height: 33px;
    color: var(--text);
  }
  .contact p { margin: 0; }
  .contact__label { color: var(--brand-red); }
</style>
</head>
<body>
  <div class="letterhead">
    <svg class="letterhead__bands" width="927" height="1200" viewBox="0 0 927 1200" aria-hidden="true">
      <path class="header-band" d="M0 0 H927 V156 C840 140 740 122 610 122 C460 122 330 152 190 162 C110 167 50 160 0 152 Z"/>
      <path class="footer-band" d="M0 1050 C80 1062 180 1068 300 1062 C450 1054 560 1038 700 1038 C800 1038 870 1044 927 1050 V1200 H0 Z"/>
    </svg>

    <header class="brand">
      <span class="brand__mark"></span>
      <span class="brand__name">Harrowfield</span>
    </header>

    <footer class="contact">
      <p><span class="contact__label">P :</span> +00 98 765 4321 <span class="contact__label">E :</span> office@harrowfield.com <span class="contact__label">W :</span> www.harrowfield.com</p>
      <p>48 Millrace Road, Cedar Bend, Iowa 50613</p>
    </footer>
  </div>
</body>
</html>
```